Etiketten-Design für Honiggläser
Zielgruppe
Imkerei Lindner
Wir sind eine Familienbetrieb und vertreiben hochwertigen Honig aus eigener Imkerei
Aufgabenstellung
Es werden Etiketten für Honiggläser benötigt
Es gibt drei verschiedene Größen von Gläser (siehe Anhang) und je größe einmal „Frühtracht“ und einmal „Sommertracht“
Also insgesamt 6 Etiketten
500g Frühtracht und Sommertracht
250g Frühtracht und Sommertracht
150g Frühtracht und Sommertracht

```html
<!DOCTYPE html>
<html lang="de">
<head>
<meta charset="utf-8">
<title>Honig Frühtracht – Etikett 500 g</title>
<link rel="stylesheet" href="https://fonts.googleapis.com/css2?family=Oswald:wght@500;600&family=Kaushan+Script&family=Open+Sans:wght@400;700&display=swap">
<style>
  :root {
    --page: #f1f1f2;
    --label: #ffffff;
    --honey: #f0a33a;
    --honey-deep: #e08a1c;
    --honey-light: #f8c866;
    --brown: #6e4a2c;
    --text-grey: #7a6a5c;
    --seal-a: #e4ecd6;
    --seal-b: #ececec;
  }
  * { margin: 0; padding: 0; box-sizing: border-box; }
  html, body {
    width: 1200px; height: 1200px; overflow: hidden;
    background: var(--page);
  }
  .canvas {
    width: 1200px; height: 1200px;
    display: flex; align-items: center; justify-content: center;
  }
  .label {
    position: relative;
    width: 1120px; height: 470px;
    background: var(--label);
    box-shadow: 0 8px 30px rgba(0,0,0,0.08);
    overflow: hidden;
  }
  .art-bees {
    position: absolute; left: 0; top: 0;
    width: 240px; height: 470px;
    background: radial-gradient(circle at 45% 45%, var(--honey-light) 0%, var(--honey) 55%, var(--honey-deep) 100%);
  }
  .art-comb {
    position: absolute; right: 0; top: 0;
    width: 300px; height: 470px;
    background: linear-gradient(160deg, var(--honey-light) 0%, var(--honey) 50%, var(--honey-deep) 100%);
  }
  .seals {
    position: absolute; left: 266px; top: 30px;
    display: flex; gap: 10px;
  }
  .seal {
    width: 48px; height: 48px; border-radius: 6px;
  }
  .seal--first { background: var(--seal-a); }
  .seal--second { background: var(--seal-b); }
  .content {
    position: absolute; left: 240px; right: 300px; top: 44px;
    text-align: center;
  }
  .brand {
    font-family: "Oswald", sans-serif; font-weight: 500;
    font-size: 26px; letter-spacing: 2px; line-height: 1.2;
    color: var(--honey); text-transform: uppercase;
  }
  .product {
    font-family: "Oswald", sans-serif; font-weight: 600;
    font-size: 104px; line-height: 1; letter-spacing: 3px;
    color: var(--honey);
    margin-top: 26px;
  }
  .variety {
    font-family: "Kaushan Script", cursive;
    font-size: 54px; color: var(--brown);
    margin-top: 10px; line-height: 1.1;
  }
  .origin {
    font-family: "Open Sans", sans-serif; font-size: 12px;
    letter-spacing: 0.5px; color: var(--text-grey);
    text-transform: uppercase; margin-top: 10px;
  }
  .details {
    font-family: "Open Sans", sans-serif; font-size: 10px;
    line-height: 1.45; color: var(--text-grey); margin-top: 10px;
  }
  .weight {
    font-family: "Open Sans", sans-serif; font-weight: 700;
    font-size: 20px; color: var(--honey); margin-top: 12px;
  }
</style>
</head>
<body>
<div class="canvas">
  <section class="label">
    <div class="art-bees" role="img" aria-label="Illustration: Bienen auf Honigwaben"></div>

    <div class="seals" aria-hidden="true">
      <div class="seal seal--first"></div>
      <div class="seal seal--second"></div>
    </div>

    <div class="content">
      <div class="brand">Imkerei Lindner</div>
      <h1 class="product">HONIG</h1>
      <div class="variety">Frühtracht</div>
      <div class="origin">Deutscher Honig aus eigener Imkerei</div>
      <div class="details">
        Imkerei Lindner · Am Bienenhof 12 · 35039 Marburg<br>
        Mindestens haltbar bis: siehe Deckel · Los-Nr. 0425<br>
        Lagerung: trocken, kühl · Ursprung: Deutschland
      </div>
      <div class="weight">netto 500 g</div>
    </div>

    <div class="art-comb" role="img" aria-label="Illustration: Honigwaben mit Honiglöffel"></div>
  </section>
</div>
</body>
</html>
```